E-Learning Directory

It's a library of links to online articles and videos that accompany 10 videos I made for a Brightfern Pitchcraft Intensive. I'm a newspaper copy-editor who has done some basic page design, so I created a rough idea of how I want these 22 pages to look (incl the placement of royalty-free photos). But it just looks a little flat, tbh. I made it in Mac Pages, but when I converted it to Word, some of the photos got lopped off. But I need it to be in Word and for all the links to be clickable. I'm also a fan of white space. So the brief, basically, is to tidy it up, keep a fair amount of white space, change the fonts to something more reader friendly, and give it more of a professional sheen. I also need to be able to make text edits afterwards myself.

Target Market(s)

Small businesses

Requirements
Must have
• Different size photos (like in PDF)
Nice to have
• White space
Should not have
• Blocky fonts

```html
<!DOCTYPE html>
<html lang="en">
<head>
<meta charset="utf-8">
<title>E-Learning Directory – Brightfern Pitchcraft Intensive study aid</title>
<link rel="stylesheet" href="https://fonts.googleapis.com/css2?family=Exo+2:wght@600&family=Tinos:ital,wght@0,400;0,700;1,400&family=Arimo&family=PT+Sans:ital,wght@0,400;0,700;1,400&display=swap">
<style>
:root{
  --brick:#a84a43;
  --heading:#a2392f;
  --ink:#2b2b2b;
  --link:#1f3fbf;
  --paper:#ffffff;
  --backdrop:#9a9a96;
}
*{box-sizing:border-box;margin:0;padding:0}
html,body{width:750px;height:1200px;overflow:hidden;background:var(--backdrop)}
.stage{position:relative;width:1250px;height:2000px;transform:scale(.6);transform-origin:0 0}
.page{position:absolute;width:413px;height:585px;background:var(--paper);overflow:hidden;box-shadow:0 2px 6px rgba(0,0,0,.25);font-family:"PT Sans",sans-serif;color:var(--ink)}
.photo{position:absolute}
.footer-band{position:absolute;left:0;right:0;top:555px;height:15px;background:var(--brick);color:#fff;font-size:7.5px;line-height:15px;padding:0 20px}
.footer-band.right{text-align:right}
.footer-band .num{font-weight:700;margin-left:6px}
.footer-band.left .num{margin:0 8px 0 0}
.section-title{position:absolute;font-family:"Tinos",serif;font-weight:700;color:var(--heading);font-size:12.5px}
.copy{position:absolute;font-size:7px;line-height:1.62}
.copy p{margin-bottom:9px}
.copy a{color:var(--link);text-decoration:underline;word-break:break-all}
.copy b{font-weight:700}
.copy.tight p{margin-bottom:4px}

/* cover */
.cover-art{left:0;top:0;width:413px;height:311px;background:radial-gradient(circle at 30% 30%,#f0a64a 0 6%,transparent 7%),radial-gradient(circle at 75% 20%,#e4572e 0 5%,transparent 6%),linear-gradient(180deg,#1aa0c4 0%,#1587b0 45%,#a9dbd8 75%,#e8f2e4 100%)}
.cover-heads{left:0;top:200px;width:413px;height:111px;background:linear-gradient(180deg,rgba(14,77,130,.55),#0e4d82)}
.brand{position:absolute;left:0;right:0;top:148px;text-align:center;font-family:"Exo 2",sans-serif;font-weight:600;font-size:38px;color:#fff}
.cover-title{position:absolute;left:0;right:0;top:326px;text-align:center;font-family:"Tinos",serif;font-weight:400;font-size:27px;color:var(--brick)}
.cover-sub{position:absolute;left:0;right:0;top:388px;text-align:center;font-family:"Arimo",sans-serif;font-size:13.5px;line-height:1.2;color:var(--brick)}
.cover-note{position:absolute;left:30px;right:30px;top:505px;font-family:"Tinos",serif;font-style:italic;font-size:5.4px;line-height:1.4;text-align:justify}
</style>
</head>
<body>
<main class="stage">

  <section class="page" style="left:640px;top:101px">
    <div class="photo cover-art" role="img" aria-label="Illustration of speech bubbles filled with idea and gear icons above silhouetted heads"></div>
    <div class="photo cover-heads" role="img" aria-label="Row of blue head silhouettes in profile"></div>
    <div class="brand">Tale &amp; Trade</div>
    <h1 class="cover-title">E-Learning Directory</h1>
    <p class="cover-sub">A Brightfern Pitchcraft Intensive<br>study aid*</p>
    <p class="cover-note">(*These videos and articles are sourced from external websites and were all checked on May XX, 2022. Taleandtrade.example obviously cannot guarantee they will still be live any time students access them after this date.)</p>
    <div class="footer-band right">E-Learning Directory &nbsp;|<span class="num">1</span></div>
  </section>

  <section class="page" style="left:196px;top:707px">
    <div class="photo" style="left:0;top:0;width:413px;height:354px;background:linear-gradient(180deg,#9fb4c9 0%,#c8d2d6 18%,#8a6a4e 35%,#b8946a 60%,#6e6a66 80%,#8c8884 100%)" role="img" aria-label="Photo of a man walking along a winding road through a dry mountain valley"></div>
    <h2 class="section-title" style="left:30px;top:381px">Introduction</h2>
    <div class="copy" style="left:30px;top:405px;width:186px">
      <p><b>Video:</b> <i>Never underestimate the power of a great story</i></p>
      <p>I love this classic ad from French TV station <b>Canal Nord</b>. It’s a very clever introduction to the message behind this course and the tale our protagonist tells is pretty much guaranteed to make you smile. And it’s very hard to argue with the tagline, but maybe I’m biased: “Never underestimate the power of a great story.”</p>
      <p><a href="https://reelshare.example/watch?v=Gd3dlXXLcdE">https://reelshare.example/watch?v=Gd3dlXXLcdE</a></p>
    </div>
    <div class="photo" style="left:228px;top:410px;width:168px;height:111px;background:radial-gradient(ellipse at 50% 70%,#c8623a 0%,#5a3a5a 35%,#14224a 75%)" role="img" aria-label="Night photo of a lit triumphal arch with traffic light trails"></div>
    <div class="footer-band left"><span class="num">2</span>|&nbsp; A Brightfern Pitchcraft Intensive &nbsp;study aid</div>
  </section>

  <section class="page" style="left:640px;top:707px">
    <h2 class="section-title" style="left:29px;top:30px">Objection(s)!</h2>
    <div class="photo" style="left:29px;top:53px;width:353px;height:195px;background:radial-gradient(ellipse at 45% 45%,#8a5a48 0%,#4a2a22 35%,#0d0b0b 75%)" role="img" aria-label="Close-up photo of a wooden judge's gavel on a dark background"></div>
    <h2 class="section-title" style="left:29px;top:270px">The Five Myths Holding You Back</h2>
    <div class="copy" style="left:29px;top:301px;width:180px">
      <p><b>Article:</b> Journaling can do us all some good. Researchers from Northvale University and Southbay University found that keeping a journal of what you’re thankful for, even if you only write in it once a week for two months, could help you feel happier… and exercise more!</p>
      <p><a href="https://dailyquill.example/entry/writing-health-benefits-journal_n_4242456">https://dailyquill.example/entry/writing-health-benefits-journal_n_4242456</a></p>
    </div>
    <div class="photo" style="left:221px;top:303px;width:161px;height:108px;background:linear-gradient(160deg,#c9cbc2 0%,#8c8f78 45%,#5a5a3a 75%,#b0703a 100%)" role="img" aria-label="Photo of a person writing in a notebook on a rock in a misty forest"></div>
    <div class="copy" style="left:29px;top:428px;width:180px">
      <p><b>Article:</b> Edwin Marsh, Jonas Holt and Felix Adler-Brand all had access to typewriters… but instead chose to write longhand when they created their works of literary genius.</p>
      <p><a href="https://ledgerweekly.example/sites/lenaharwick/2016/05/15/three-ways-that-writing-with-a-pen-positively-affects-your-brain/?sh=5ea0c5cc5705">https://ledgerweekly.example/sites/lenaharwick/2016/05/15/three-ways-that-writing-with-a-pen-positively-affects-your-brain/?sh=5ea0c5cc5705</a></p>
    </div>
    <div class="photo" style="left:221px;top:420px;width:161px;height:113px;background:linear-gradient(150deg,#6a6a6a 0%,#3a3a3a 45%,#8a8580 75%,#d2b8a8 100%)" role="img" aria-label="Photo of hands at a vintage typewriter"></div>
    <div class="footer-band right">E-Learning Directory &nbsp;|<span class="num">3</span></div>
  </section>

  <section class="page" style="left:196px;top:1315px">
    <div class="photo" style="left:0;top:0;width:413px;height:585px;background:radial-gradient(ellipse at 48% 18%,#8fb07a 0%,#c8d6bc 22%,transparent 40%),radial-gradient(ellipse at 48% 38%,#5a5a5a 0%,#bdbdbd 14%,transparent 24%),linear-gradient(180deg,#ffffff 0%,#f7f7f7 55%,#f2f2f2 62%,#2a2a2a 78%,#3a3a3a 100%)" role="img" aria-label="Soft-focus photo of a potted plant above a black paperback book about writing"></div>
    <div class="copy tight" style="left:30px;top:133px;width:352px">
      <p style="width:142px">You might protest that today’s authors are very unlikely to do so, given how far technology has come.</p>
      <p>Tell that to Harlan Ross.</p>
      <p style="width:142px">He famously wrote Nightweaver in cursive over six months while recuperating from a 1999 car accident.</p>
      <p style="width:142px">His leg was in a painful brace and sitting down at a desk to tap away on a typewriter was just too painful for him.</p>
      <p>He picked up a Marlowe pen… <i>et voila</i>. “Suddenly I had this huge, huge book… I didn’t think about the pain as much. It’s like being hypnotized,” he said.</p>
      <p style="margin-bottom:9px">He even once called a fountain pen “the world’s finest word processor”.</p>
      <p><a href="https://inkwellhouse.example/blogs/the-jotted-line/harlan-ross-fountain-pen">https://inkwellhouse.example/blogs/the-jotted-line/harlan-ross-fountain-pen</a></p>
    </div>
  </section>

  <section class="page" style="left:640px;top:1315px">
    <div class="photo" style="left:0;top:0;width:413px;height:257px;background:radial-gradient(ellipse at 70% 20%,#c8d4f0 0%,#5a6ab0 30%,#1a1d3a 65%),#101020" role="img" aria-label="Photo of a concert crowd raising hands under stage lights"></div>
    <h2 class="section-title" style="left:29px;top:270px">Engaging Our Audience</h2>
    <div class="copy" style="left:29px;top:303px;width:182px">
      <p><b>Video:</b> <i>Brotherly Law: I Have a Case</i></p>
      <p>You only need to watch the first 30 seconds of this clip to see the classic quote I want to point out here… “Explain it to me like I’m a six-year-old.”</p>
      <p>Anytime you’re talking to somebody and they tell you what their job is but you still can’t quite get to grips with it… just get them to explain it to you as if you’re six and tell them you won’t be insulted. It’s amazing the clarity this brings.</p>
      <p>As for Philadelphia itself, it’s called the City of Brotherly Love because it’s a combination of the Greek words <i>phileo</i> (love) and <i>adelphos</i> (brother). It was named by founder Thomas Ashford, who envisioned a city of religious tolerance.</p>
      <p><a href="https://reelshare.example/watch?v=XUysELdf3Cw">https://reelshare.example/watch?v=XUysELdf3Cw</a></p>
    </div>
    <div class="photo" style="left:238px;top:270px;width:175px;height:263px;background:linear-gradient(180deg,#d8dce2 0%,#c84a3a 12%,#d64a3a 38%,#8a7a6a 55%,#b8d0d8 75%,#4a7a4a 100%)" role="img" aria-label="Photo of a red letter sculpture above a fountain with a child in a green shirt"></div>
    <div class="footer-band right">E-Learning Directory &nbsp;|<span class="num">5</span></div>
  </section>

</main>
</body>
</html>
```